Business Card Design - Palorin

Please see our website www.palorin-example.com.au

We supply high quality natural therapeutic medications to animal health care providers such as Veterinary clinics & saddlery stores.

Our main product we distribute is Burimosa for horses, dogs and cats, which is an arthritis supplement.

Feel free to use images below in the design we have the rights to use them.

A quote for the job would be great too please.

It would be good to stick with the colour theme of our website if possible please.

Thanks,

Glen

Hi Folks, Apologies, I made a mistake with the contact no. in the opening brief. It should be 0400 555 913 (not 0400 555 276 which is my private practice office number.) Thanks for your submissions, much appreciated and several under serious consideration, Glen

Target Market(s)

Veterinary clinics, saddlery stores, produce stores.

Industry/Entity Type

Health

Contact Information for Business Card

orders@palorin-example.net
www.palorin-example.com.au
ph. 0400 555 913
ABN 98 000 555 317 (SMALL SIZE)

Colors
b768aa

Requirements
Should not have
• My name (Dr Glen Harcourt)

```html
<!DOCTYPE html>
<html lang="en">
<head>
<meta charset="utf-8">
<title>Palorin — Business Card</title>
<link href="https://fonts.googleapis.com/css2?family=Open+Sans:ital,wght@0,400;0,600;0,700;1,400&display=swap" rel="stylesheet">
<style>
  :root {
    --page-bg: #eeeeee;
    --brand-violet: #8a1fe0;
    --band-purple: rgba(118, 58, 150, 0.86);
    --band-text: #ffffff;
    --logo-white: #ffffff;
    --tagline-ink: #2b2230;
    --photo-light: #f1ece8;
    --photo-fur: #d6ad7c;
    --photo-skin: #e9c29a;
    --photo-shirt: #7a4a90;
  }
  * { margin: 0; padding: 0; box-sizing: border-box; }
  html, body {
    width: 1200px;
    height: 900px;
    overflow: hidden;
    background: var(--page-bg);
    font-family: "Open Sans", Arial, sans-serif;
  }
  .canvas {
    width: 1200px;
    height: 900px;
    display: flex;
    align-items: center;
    justify-content: center;
  }
  .business-card {
    position: relative;
    width: 1050px;
    height: 600px;
    overflow: hidden;
    box-shadow: 0 10px 30px rgba(0, 0, 0, 0.18);
  }
  .card-photo {
    position: absolute;
    inset: 0;
    background:
      radial-gradient(ellipse 30% 40% at 28% 45%, var(--photo-fur) 0%, rgba(214,173,124,0) 100%),
      radial-gradient(ellipse 28% 45% at 72% 52%, var(--photo-skin) 0%, rgba(233,194,154,0) 100%),
      radial-gradient(ellipse 45% 30% at 60% 100%, var(--photo-shirt) 0%, rgba(122,74,144,0) 100%),
      linear-gradient(180deg, var(--photo-light) 0%, #e4dbd2 100%);
  }
  .website {
    position: absolute;
    top: 26px;
    left: 38px;
    font-size: 26px;
    font-weight: 700;
    color: var(--brand-violet);
    letter-spacing: 0.2px;
  }
  .brand {
    position: absolute;
    top: 258px;
    left: 380px;
  }
  .brand-name {
    font-size: 76px;
    font-weight: 700;
    color: var(--logo-white);
    line-height: 1;
    letter-spacing: -0.5px;
  }
  .brand-tagline {
    margin-top: 6px;
    margin-left: 20px;
    font-size: 27px;
    font-style: italic;
    color: var(--tagline-ink);
  }
  .contact-band {
    position: absolute;
    left: 0;
    right: 0;
    bottom: 0;
    height: 66px;
    background: var(--band-purple);
    display: flex;
    align-items: center;
    justify-content: space-between;
    padding: 0 34px;
    color: var(--band-text);
  }
  .contact-main {
    font-size: 24px;
    font-weight: 600;
  }
  .contact-divider { margin: 0 18px; }
  .abn {
    font-size: 20px;
    font-weight: 400;
  }
</style>
</head>
<body>
  <main class="canvas">
    <article class="business-card">
      <div class="card-photo" role="img" aria-label="Photograph of a smiling young woman with short blonde hair cuddling a fluffy tan dog"></div>
      <p class="website">www.palorin-example.com.au</p>
      <div class="brand">
        <p class="brand-name">palorin</p>
        <p class="brand-tagline">natural therapeutic medications</p>
      </div>
      <footer class="contact-band">
        <p class="contact-main">orders@palorin-example.net<span class="contact-divider">/</span>Ph.: 0400 555 913</p>
        <p class="abn">ABN 98 000 555 317</p>
      </footer>
    </article>
  </main>
</body>
</html>
```